Lantern Ridge Tile Inc. Business Card

Looking for business card with embossed raised logo print. Logo provided and want it to be most prominent image on card. Color pallet of black, red, white or charcoal gray preferred for brand recognition. Simple contact information on front and list description of services provided on back. Services included....Custom Showers, Tub Surrounds, Backsplashes, Fireplaces, Floors and more. Dustless Demolition, Lifetime Warranty, Proud member of the Federated Stoneworks Trade Guild

Target Market(s)

High end residential remodel work and new home builders

Contact Information for Business Card

Phone # (402) 555-0193 email address, Lanternridgets@mailvane.net Colby Hanswirth Owner

Requirements
Must have
• Business logo as most prominent image on the front of business card. Along with contact information and name Colby Hanswirth. Would like to see services provided on the back of the card.

```html
<!DOCTYPE html>
<html lang="en">
<head>
<meta charset="UTF-8">
<title>Lantern Ridge Tile Inc. Business Card</title>
<link href="https://fonts.googleapis.com/css2?family=Quicksand:wght@500;600;700&family=Courgette&display=swap" rel="stylesheet">
<style>
  :root {
    --red: #d8212b;
    --white: #ffffff;
    --paper: #f2f2f2;
    --charcoal: #333335;
    --backdrop: #d9d9db;
  }
  * { margin: 0; padding: 0; box-sizing: border-box; }
  html, body { width: 1200px; height: 900px; overflow: hidden; }
  body {
    background: var(--backdrop);
    font-family: "Quicksand", sans-serif;
    position: relative;
  }
  .card {
    position: absolute;
    left: 285px;
    width: 630px;
    height: 360px;
    border-radius: 26px;
    overflow: hidden;
    box-shadow: 0 10px 26px rgba(0,0,0,0.25);
  }
  .card-back { top: 65px; background: var(--red); color: var(--white); }
  .card-front { top: 475px; background: linear-gradient(135deg, var(--white), var(--paper)); }

  .brand {
    position: absolute;
    display: flex;
    align-items: center;
    gap: 14px;
    font-weight: 700;
    letter-spacing: 1px;
    line-height: 1.05;
  }
  .brand-mark { width: 44px; height: 44px; flex: none; }
  .brand-name { font-size: 30px; text-transform: uppercase; }
  .brand-name small { display: block; font-size: 15px; letter-spacing: 4px; }

  .card-back .brand { left: 40px; top: 42px; color: var(--white); }
  .card-back .brand-mark { background: var(--white); }

  .services {
    position: absolute;
    right: 40px;
    top: 100px;
    text-align: right;
    font-weight: 500;
    font-size: 19px;
    line-height: 1.45;
  }
  .services-title { font-size: 23px; font-weight: 600; margin-bottom: 4px; }

  .membership {
    position: absolute;
    left: 40px;
    right: 40px;
    bottom: 38px;
    font-family: "Courgette", cursive;
    font-size: 19px;
    border-top: 1px solid rgba(255,255,255,0.6);
    padding-top: 10px;
    text-align: right;
  }

  .front-wave { position: absolute; inset: 0; width: 630px; height: 360px; }
  .card-front .brand { left: 56px; top: 96px; color: var(--red); }
  .card-front .brand-mark { background: var(--red); }
  .card-front .brand-name { font-size: 32px; }
  .card-front .brand-name small { font-size: 16px; }

  .contact-icon { position: absolute; right: 34px; width: 30px; height: 30px; }
  .icon-phone { top: 132px; }
  .icon-email { top: 222px; }
  .contact-line {
    position: absolute;
    right: 34px;
    color: var(--white);
    font-weight: 600;
    white-space: nowrap;
  }
  .contact-phone { top: 168px; font-size: 26px; }
  .contact-email { top: 256px; font-size: 22px; }
  .contact-owner { top: 302px; font-size: 17px; font-weight: 500; }
</style>
</head>
<body>

<section class="card card-back">
  <div class="brand">
    <span class="brand-mark"></span>
    <span class="brand-name">Lantern Ridge<small>Tile Inc</small></span>
  </div>
  <div class="services">
    <div class="services-title">Services Included</div>
    <div>Custom Showers, Tub Surrounds</div>
    <div>Backsplashes, Fireplaces</div>
    <div>Floors and more</div>
    <div>Dustless Demolition</div>
    <div>Lifetime Warranty</div>
  </div>
  <p class="membership">Proud member of the Federated Stoneworks Trade Guild</p>
</section>

<section class="card card-front">
  <svg class="front-wave" viewBox="0 0 630 360" aria-hidden="true">
    <path d="M630,80 C520,80 468,94 436,134 C396,194 346,224 0,228" fill="none" stroke="var(--charcoal)" stroke-width="12"/>
    <path d="M630,96 C520,96 470,110 440,150 C400,210 350,240 0,244 L0,360 L630,360 Z" fill="var(--red)"/>
  </svg>
  <div class="brand">
    <span class="brand-mark"></span>
    <span class="brand-name">Lantern Ridge<small>Tile Inc</small></span>
  </div>

  <svg class="contact-icon icon-phone" viewBox="0 0 30 30" aria-hidden="true">
    <circle cx="15" cy="15" r="13" fill="none" stroke="var(--white)" stroke-width="2"/>
    <path d="M11 8 l3 0 l1 4 l-2 1.5 q1.5 3 4 4.5 l1.5 -2 l4 1 l0 3 q-8 1 -12 -12 z" fill="var(--white)"/>
  </svg>
  <div class="contact-line contact-phone">(402) 555-0193</div>

  <svg class="contact-icon icon-email" viewBox="0 0 30 30" aria-hidden="true">
    <circle cx="15" cy="15" r="13" fill="none" stroke="var(--white)" stroke-width="2"/>
    <rect x="8" y="10" width="14" height="10" fill="none" stroke="var(--white)" stroke-width="1.6"/>
    <path d="M8 10 L15 16 L22 10" fill="none" stroke="var(--white)" stroke-width="1.6"/>
  </svg>
  <div class="contact-line contact-email">Lanternridgets@mailvane.net</div>

  <div class="contact-line contact-owner">Colby Hanswirth, Owner</div>
</section>

</body>
</html>
```